Life Coaching and Career Coaching company needs new website with bold, modern, videos

We need a whole new website that is heavy on video. We are a small company who sells personal wellbeing services like career coaching, life coaching, and group coaching programs. The programs all help people design a better life.
FULL BRIEF ATTACHED and STYLE GUIDE
Also, look at https://www.pinevaultery.com/coaching and corvanly.com and https://www.tarnwick.life/ for a small amount of inspiration.

Industry/Entity Type

personal well-being/life coaching/career coaching

Number of Pages Required

3 page

Other font styles liked:
• fonts are in the brief

Requirements
Must have
• read the brief please - it's all in there. (things like the look, feel, how it will have lots of video, etc,)
Nice to have
• something really different looking and breakthrough. visually stunning. very trustworthy. Please read the brief, its all in there.
Should not have
• should not look like other life coaching websites. must have video!

```html
<!DOCTYPE html>
<html lang="en">
<head>
<meta charset="utf-8">
<title>Larkfield Studio — Coaching</title>
<link href="https://fonts.googleapis.com/css2?family=Righteous&family=Questrial&family=Montserrat:wght@600;700&display=swap" rel="stylesheet">
<style>
:root{
  --coral:#ef6b6b;
  --plum:#4a0f4a;
  --wine:#8e1f24;
  --wine-dark:#7a171c;
  --ink:#1e1e1e;
  --text:#333;
  --footer:#262626;
  --white:#fff;
}
*{margin:0;padding:0;box-sizing:border-box}
html,body{width:1200px;height:3604px;overflow:hidden}
body{position:relative;background:var(--white);font-family:"Questrial",sans-serif;color:var(--text)}
.abs{position:absolute}
.display{font-family:"Righteous",sans-serif;text-transform:uppercase;letter-spacing:.5px}
.nav-label{font-family:"Montserrat",sans-serif;font-weight:600;font-size:16px;text-transform:uppercase}

/* header */
.site-header{left:0;top:0;width:1200px;height:96px;background:var(--coral)}
.brand{left:172px;top:22px;width:266px;color:var(--white);font-family:"Questrial",sans-serif;font-size:27px;line-height:1;letter-spacing:.5px;white-space:nowrap}
.brand small{display:block;text-align:right;font-size:15px;margin-top:4px;letter-spacing:1px}
.main-nav a{position:absolute;top:37px;color:var(--white);text-decoration:none;white-space:nowrap}
.signup{left:949px!important;top:31px!important;width:79px;height:33px;background:var(--white);color:var(--ink)!important;text-align:center;line-height:33px}

/* hero */
.hero-media{left:0;top:96px;width:1200px;height:680px;background:radial-gradient(ellipse at 30% 55%,#5a4a3e 0%,#2a2030 40%,#120e1c 75%);}
.hero-mark{right:172px;top:176px;color:var(--white);font-size:74px;line-height:1;white-space:nowrap}
.hero-title{right:172px;top:340px;color:var(--white);font-size:46px;line-height:48px;text-align:right;white-space:nowrap}
.hero-play{left:932px;top:472px}

/* programs */
.programs-band{left:0;top:670px;width:1200px;height:666px}
.section-title-light{left:0;width:1200px;top:818px;text-align:center;color:var(--white);font-size:44px}
.program-card{top:914px;width:280px;height:327px;background:var(--white);text-align:center}
.program-card .media{height:220px}
.card-title{font-family:"Montserrat",sans-serif;font-weight:600;font-size:18px;color:var(--ink);text-transform:uppercase;margin-top:20px;white-space:nowrap}
.card-text{font-size:14px;line-height:21px;color:var(--ink);padding:4px 10px 0}

/* testimonials */
.testi-title{left:0;width:1200px;top:1395px;text-align:center;color:var(--plum);font-size:44px}
.testi-intro{left:218px;width:764px;top:1458px;text-align:center;font-size:14px;line-height:21px;color:var(--ink)}
.video-card{background:var(--white);box-shadow:0 2px 8px rgba(0,0,0,.18)}
.video-card .media{position:absolute;left:0;top:0}
.video-feature{left:172px;top:1530px;width:465px;height:467px}
.video-feature .media{width:465px;height:360px;background:linear-gradient(135deg,#8a7c70,#c9b7a3 50%,#6d635c)}
.video-feature .card-title{position:absolute;top:376px;width:100%;text-align:center;margin:0}
.video-feature .card-text{position:absolute;top:408px;width:100%;padding:0 30px;text-align:center}
.video-small{left:648px;width:380px;height:225px}
.video-small .media{width:199px;height:225px}
.video-small .body{position:absolute;left:211px;top:24px;width:160px}
.video-small .card-title{font-size:15px;margin:0 0 8px;text-align:left;letter-spacing:-.2px}
.video-small .card-text{padding:0;font-size:12.5px;line-height:21px;text-align:justify}
.play-icon{position:absolute}

/* about band */
.about-band{left:0;top:2060px;width:1200px;height:640px}
.about-col{top:2168px;width:396px;color:var(--white)}
.about-col .icon{width:110px;height:112px;background:rgba(255,255,255,.25);border-radius:8px}
.about-col h2{font-size:40px;margin-top:40px;line-height:1;white-space:nowrap}
.about-col p{font-size:15px;line-height:21px;text-align:justify;margin-top:12px}
.about-col p+p{margin-top:8px}
.btn{display:inline-block;font-family:"Montserrat",sans-serif;font-weight:700;font-size:16px;text-transform:uppercase;padding:0 9px;height:40px;line-height:40px;text-decoration:none}
.btn-light{background:var(--white);color:var(--ink);margin-top:26px}
.btn-plum{background:var(--plum);color:var(--white);margin-top:26px}

/* experience */
.experience-media{left:600px;top:2640px;width:600px;height:569px;background:linear-gradient(90deg,#f2f1ef 0%,#d9d3c9 25%,#b8aa98 60%,#6f7a55 100%)}
.experience-bg{left:0;top:2640px;width:620px;height:569px;background:linear-gradient(90deg,#fafafa,#f1f0ee)}
.experience-copy{left:172px;top:2785px;width:396px;color:var(--ink)}
.experience-copy h2{font-size:40px;line-height:48px;color:var(--ink);white-space:nowrap}
.experience-copy p{font-size:15px;line-height:21px;text-align:justify;margin-top:22px}
.experience-copy p+p{margin-top:10px}

/* footer */
.site-footer{left:0;top:3209px;width:1200px;height:395px;background:var(--footer);color:var(--white)}
.footer-brand{right:731px;top:84px;text-align:right;font-size:54px;line-height:60px;white-space:nowrap}
.footer-brand small{display:block;font-size:28px;line-height:34px}
.footer-col{top:106px}
.footer-col h3{font-family:"Righteous",sans-serif;font-size:20px;text-transform:uppercase;font-weight:400}
.quick-links{left:603px}
.quick-links a{display:block;color:var(--white);text-decoration:none;font-family:"Montserrat",sans-serif;font-weight:600;font-size:13px;margin-top:16px;line-height:15px}
.quick-links h3+a{margin-top:24px}
.contact{left:820px}
.contact li{list-style:none;display:flex;gap:10px;font-family:"Montserrat",sans-serif;font-weight:600;font-size:13px;line-height:22px;margin-top:14px;white-space:nowrap}
.contact h3+ul li:first-child{margin-top:20px}
.contact svg{flex:none;margin-top:4px}
.footer-rule{left:172px;top:308px;width:856px;height:1px;background:#cfcfcf}
.copyright{left:0;width:1200px;top:340px;text-align:center;font-size:14px;font-family:"Montserrat",sans-serif;font-weight:600}
</style>
</head>
<body>

<header class="site-header abs">
  <div class="brand abs">LARKFIELD STUDIO<small>COACHING</small></div>
  <nav class="main-nav">
    <a class="nav-label" style="left:548px" href="#">Jobs</a>
    <a class="nav-label" style="left:616px" href="#">Companies</a>
    <a class="nav-label" style="left:741px" href="#">Advice</a>
    <a class="nav-label" style="left:830px" href="#">Coaching</a>
    <a class="nav-label signup abs" href="#">Signup</a>
  </nav>
</header>

<section class="hero">
  <div class="hero-media abs" role="img" aria-label="Photo of a man speaking at a wooden podium with a laptop and microphone in a dim auditorium"></div>
  <div class="hero-mark abs display">Larkfield</div>
  <h1 class="hero-title abs display">Watch a first<br>coaching session</h1>
  <svg class="hero-play abs" width="96" height="96" viewBox="0 0 96 96" aria-label="Play video">
    <circle cx="48" cy="48" r="44" fill="none" stroke="#fff" stroke-width="5"/>
    <path d="M38 30 L66 48 L38 66 Z" fill="#fff"/>
  </svg>
</section>

<svg class="programs-band abs" width="1200" height="666" viewBox="0 0 1200 666">
  <path d="M0 0 Q600 160 1200 0 L1200 666 L0 666 Z" fill="var(--plum)"/>
  <path d="M0 0 Q600 160 1200 0" fill="none" stroke="var(--coral)" stroke-width="7"/>
</svg>

<h2 class="section-title-light abs display">Our programs</h2>

<article class="program-card abs" style="left:17px">
  <div class="media" role="img" aria-label="Photo of a smiling woman seated in an office lounge" style="background:linear-gradient(135deg,#b44 0%,#9a8a7a 40%,#575350)"></div>
  <h3 class="card-title">Nemo enim ipsam</h3>
  <p class="card-text">Neque porro quisquam est, qui dolor em ipsum quia dolor sit amet</p>
</article>
<article class="program-card abs" style="left:313px">
  <div class="media" role="img" aria-label="Photo of a woman presenting at a podium to a seated audience" style="background:linear-gradient(135deg,#1b1a2c,#3a3348 50%,#8a6a40)"></div>
  <h3 class="card-title">Nemo enim ipsam</h3>
  <p class="card-text">Neque porro quisquam est, qui dolor em ipsum quia dolor sit amet</p>
</article>
<article class="program-card abs" style="left:609px">
  <div class="media" role="img" aria-label="Photo of a stage with a bright screen seen from behind the audience" style="background:linear-gradient(180deg,#3a3f8a,#7a4aa0 40%,#1a1630)"></div>
  <h3 class="card-title">Nemo enim ipsam</h3>
  <p class="card-text">Neque porro quisquam est, qui dolor em ipsum quia dolor sit amet</p>
</article>
<article class="program-card abs" style="left:904px">
  <div class="media" role="img" aria-label="Photo of a woman working on a laptop at a desk" style="background:linear-gradient(135deg,#e9e6e2,#b89a88 45%,#8a2a2e)"></div>
  <h3 class="card-title">Nemo enim ipsam</h3>
  <p class="card-text">Neque porro quisquam est, qui dolor em ipsum quia dolor sit amet</p>
</article>

<h2 class="testi-title abs display">Video testimonials</h2>
<p class="testi-intro abs">Sed ut perspiciatis unde omnis iste natus error sit voluptatem accusantium doloremque laudantium, totam rem aperiam, eaque ipsa quae ab illo inventore veritatis et quasi architecto beatae</p>

<article class="video-card video-feature abs">
  <div class="media" role="img" aria-label="Video still of a smiling woman at a desk with a laptop and coffee cup"></div>
  <svg class="play-icon" style="left:186px;top:134px" width="94" height="94" viewBox="0 0 94 94" aria-label="Play video">
    <circle cx="47" cy="47" r="43" fill="rgba(0,0,0,.15)" stroke="#fff" stroke-width="5"/>
    <path d="M38 30 L64 47 L38 64 Z" fill="#fff"/>
  </svg>
  <h3 class="card-title">Nemo enim ipsam</h3>
  <p class="card-text">Neque porro quisquam est, qui dolor em ipsum quia dolor sit amet porro quisquam</p>
</article>

<article class="video-card video-small abs" style="top:1530px">
  <div class="media" role="img" aria-label="Video still of a woman in a dark blazer in an office" style="background:linear-gradient(135deg,#d9dcdf,#7a6a62 55%,#222)"></div>
  <svg class="play-icon" style="left:72px;top:86px" width="54" height="54" viewBox="0 0 54 54" aria-label="Play video">
    <circle cx="27" cy="27" r="24" fill="rgba(0,0,0,.15)" stroke="#fff" stroke-width="3"/>
    <path d="M22 17 L37 27 L22 37 Z" fill="#fff"/>
  </svg>
  <div class="body">
    <h3 class="card-title">Nemo enim ipsam</h3>
    <p class="card-text">Neque porro quisquam est, qui dolor em ipsum quia dolor sit amet porro quisquam. Neque porro quisquam est, qui dolor em ipsum quia dolor sit amet porro quisquam.</p>
  </div>
</article>

<article class="video-card video-small abs" style="top:1772px">
  <div class="media" role="img" aria-label="Video still of an older woman in a teal cardigan holding a mug" style="background:linear-gradient(135deg,#e8e6e3,#b99a86 45%,#1f6f80)"></div>
  <svg class="play-icon" style="left:72px;top:86px" width="54" height="54" viewBox="0 0 54 54" aria-label="Play video">
    <circle cx="27" cy="27" r="24" fill="rgba(0,0,0,.15)" stroke="#fff" stroke-width="3"/>
    <path d="M22 17 L37 27 L22 37 Z" fill="#fff"/>
  </svg>
  <div class="body">
    <h3 class="card-title">Nemo enim ipsam</h3>
    <p class="card-text">Neque porro quisquam est, qui dolor em ipsum quia dolor sit amet porro quisquam. Neque porro quisquam est, qui dolor em ipsum quia dolor sit amet porro quisquam.</p>
  </div>
</article>

<svg class="about-band abs" width="1200" height="640" viewBox="0 0 1200 640" role="img" aria-label="Faint photo of a seminar room behind a deep red band">
  <defs>
    <linearGradient id="aboutTone" x1="0" y1="0" x2="0" y2="1">
      <stop offset="0" stop-color="#8e1f24"/>
      <stop offset=".45" stop-color="#942a2e"/>
      <stop offset=".75" stop-color="#7d1a1f"/>
      <stop offset="1" stop-color="#8e1f24"/>
    </linearGradient>
  </defs>
  <path d="M0 89 Q600 -65 1200 89 L1200 551 Q600 705 0 551 Z" fill="url(#aboutTone)"/>
</svg>

<div class="about-col abs" style="left:172px">
  <div class="icon" role="img" aria-label="Line illustration of a person with a speech bubble"></div>
  <h2 class="display">Who we are</h2>
  <p>Sed ut perspiciatis unde omnis iste natus error sit voluptatem accusantium doloremque laudantium, totam rem aperiam, eaque ipsa quae ab illo inventore veritatis et quasi architecto beatae.</p>
  <p>Quis autem vel eum iure reprehenderit qui in ea voluptate velit esse quam nihil molestiae consequatur, vel illum qui dolorem eum fugiat quo voluptas nulla pariatur.</p>
  <a class="btn btn-light" href="#">Read more</a>
</div>
<div class="about-col abs" style="left:633px">
  <div class="icon" style="width:122px" role="img" aria-label="Line illustration of a computer monitor with a cursor"></div>
  <h2 class="display">Our programs</h2>
  <p>Sed ut perspiciatis unde omnis iste natus error sit voluptatem accusantium doloremque laudantium, totam rem aperiam, eaque ipsa quae ab illo inventore veritatis et quasi architecto beatae.</p>
  <p>Quis autem vel eum iure reprehenderit qui in ea voluptate velit esse quam nihil molestiae consequatur, vel illum qui dolorem eum fugiat quo voluptas nulla pariatur.</p>
  <a class="btn btn-light" href="#">Read more</a>
</div>

<section class="experience">
  <div class="experience-bg abs"></div>
  <div class="experience-media abs" role="img" aria-label="Photo of a thoughtful businesswoman at a desk with papers and plants"></div>
  <svg class="abs" style="left:0;top:2611px" width="1200" height="90" viewBox="0 0 1200 90">
    <path d="M0 0 Q600 154 1200 0 L1200 -10 L0 -10 Z" fill="var(--wine)"/>
  </svg>
  <div class="experience-copy abs">
    <h2 class="display">Experience that<br>matters</h2>
    <p>Sed ut perspiciatis unde omnis iste natus error sit voluptatem accusantium doloremque laudantium, totam rem aperiam, eaque ipsa quae ab illo inventore veritatis et quasi architecto beatae.</p>
    <p>Quis autem vel eum iure reprehenderit qui in ea voluptate velit esse quam nihil molestiae consequatur, vel illum qui dolorem eum fugiat quo voluptas nulla pariatur.</p>
    <a class="btn btn-plum" href="#">Read more</a>
  </div>
</section>

<footer class="site-footer abs">
  <div class="footer-brand abs">LARKFIELD<br>STUDIO<small>COACHING</small></div>
  <div class="footer-col quick-links abs">
    <h3>Quick links</h3>
    <a href="#">JOBS</a>
    <a href="#">COMPANIES</a>
    <a href="#">ADVICE</a>
    <a href="#">COACHING</a>
  </div>
  <div class="footer-col contact abs">
    <h3>Contact us</h3>
    <ul>
      <li><svg width="16" height="16" viewBox="0 0 16 16"><path d="M8 1a5 5 0 0 0-5 5c0 4 5 9 5 9s5-5 5-9a5 5 0 0 0-5-5z" fill="none" stroke="#fff" stroke-width="1.5"/><circle cx="8" cy="6" r="1.8" fill="none" stroke="#fff" stroke-width="1.5"/></svg><span>48 Harlow Ave., 3rd Floor,<br>Easton 20418</span></li>
      <li><svg width="16" height="16" viewBox="0 0 16 16"><path d="M3 1.5l3 .5 1 3-2 1.5a9 9 0 0 0 4.5 4.5L11 9l3 1 .5 3c-1 1.5-3 1.5-5 .5A14 14 0 0 1 2 6c-1-2-.5-3.5 1-4.5z" fill="none" stroke="#fff" stroke-width="1.4"/></svg><span>Phone: 555-014-2207</span></li>
      <li><svg width="16" height="16" viewBox="0 0 16 16"><rect x="1.5" y="3" width="13" height="10" fill="none" stroke="#fff" stroke-width="1.4"/><path d="M1.5 3.5L8 9l6.5-5.5" fill="none" stroke="#fff" stroke-width="1.4"/></svg><span>hello@larkfieldstudio.com</span></li>
    </ul>
  </div>
  <div class="footer-rule abs"></div>
  <p class="copyright abs">COPYRIGHTS @ 2023 LARKFIELD STUDIO.</p>
</footer>

</body>
</html>
```